TRV Electrical – Fridge Magnet & Letterbox Leaflet

Overview
We are a local electrical contractor based in Gooseberry Hill in the Perth Hills (Western Australia).
We are looking for a designer to create:
1️⃣ A fridge magnet design
2️⃣ A matching letterbox leaflet (A6 or DL)
The goal is to create clean, professional marketing that feels local and trustworthy, not flashy advertising.
The designs must feel like a high-quality local trades business, appealing to homeowners in suburbs such as:
Kalamunda
Gooseberry Hill
Lesmurdie
Walliston
Pickering Brook
Design Style
The design should feel:
✔ Local
✔ Authentic
✔ Professional
✔ Trustworthy
✔ Clean and simple
NOT:
✖ Cheap advertising
✖ Overly flashy
✖ Busy or cluttered
Think premium local tradesman, not mass marketing.
Branding
Use our brand colours inspired by our van:
Primary colours
Navy Blue
White
Accent colour
Yellow / gold highlight
Design should match the look of our work van branding.
Images Provided
We will provide:
✔ Company logo
✔ Photo of our branded van in the Perth Hills
The van photo should be used in the leaflet design to reinforce our local presence.
Fridge Magnet Design
Size suggestion:
90mm x 55mm
Purpose:
Homeowners keep this magnet so they can easily call a trusted electrician.
Must include:
TRV Electrical Contracting
Local Perth Hills Electrician
Based in Gooseberry Hill
Phone number (large and clear)
📞 0472 615 904
Services:
• Fault finding
• Switchboard upgrades
• Lighting & power
• Ceiling fans
• Smoke alarm compliance
Also include:
⭐ 110+ Rovlix Reviews
Website:
www.trvelectrical-example.com.au
Design should be very simple and easy to read from across a kitchen.
Leaflet Design
Size options:
A6 or DL
Purpose:
Letterbox drop marketing in Perth Hills suburbs.
Front Side
Headline:
WE'RE WORKING IN YOUR AREA
Subtext:
Local electrician based in Gooseberry Hill
Include:
✔ Photo of our van
✔ TRV logo
✔ Key services
Services:
• Fault finding
• Switchboard upgrades
• Lighting & power
• Ceiling fans
• Smoke alarm compliance
Call to action:
📞 Call Dorian – 0472 615 904
⭐ 110+ Five-Star Rovlix Reviews
Back Side
Headline:
Your Local Perth Hills Electrician
Servicing:
Kalamunda
Gooseberry Hill
Lesmurdie
Walliston
Pickering Brook
Short message:
Reliable electrical work across the Perth Hills.
Call Dorian
📞 0472 615 904
Website:
www.trvelectrical-example.com.au
EC47286
Target Audience
Homeowners in the Perth Hills aged 35–70.
Many homes are older properties and often need electrical upgrades, repairs and safety work.
Design should appeal to homeowners who value reliability and local service.
Deliverables
Designers must provide:
✔ Print-ready files
✔ Editable source files
✔ High resolution files
For:
Fridge magnet
Leaflet front and back
Final Notes
This design should communicate:
✔ Trusted local electrician
✔ Established business
✔ Professional service
✔ Easy to contact
The goal is to create marketing people will keep, not throw away.

```html
<!DOCTYPE html>
<html lang="en">
<head>
<meta charset="utf-8">
<title>TRV Electrical – Letterbox Leaflet</title>
<link rel="stylesheet" href="https://fonts.googleapis.com/css2?family=Poppins:wght@500;700;800&family=Arimo:wght@400;700&display=swap">
<style>
:root{
  --navy:#0d2a5c;
  --navy-deep:#0a2150;
  --gold:#fbbf21;
  --gold-deep:#f2ac12;
  --white:#ffffff;
  --ink:#111111;
  --rule:#9a9a9a;
  --stage:#9b9b9b;
}
*{box-sizing:border-box;margin:0;padding:0}
html,body{width:1200px;height:862px;overflow:hidden}
body{background:var(--stage);position:relative;font-family:"Arimo",Arial,sans-serif}
.leaflet{position:absolute;top:86px;width:513px;height:725px;background:var(--white);transform:scale(.922);transform-origin:top left;overflow:hidden}
.leaflet--front{left:97px}
.leaflet--back{left:617px}
.frame{position:absolute;inset:0}
.hero{position:absolute;left:0;top:0;width:513px;height:250px}
.hero--van{background:linear-gradient(180deg,#bcd3e6 0%,#9fb3a3 35%,#5d6b4c 60%,#1b2a48 75%,#6a5a3c 100%)}
.hero--switchboard{background:linear-gradient(110deg,#10204a 0%,#1f3f86 40%,#2a4b9c 60%,#0e1c42 100%)}
.brand{position:absolute;left:0;right:0;display:flex;justify-content:center;align-items:center;gap:10px}
.brand__mark{width:38px;height:50px;background:var(--navy)}
.brand__name{font-family:"Poppins",sans-serif;font-weight:500;color:var(--navy);font-size:17px;line-height:22px;width:130px}
.brand__name--small{font-size:15px;line-height:19px;width:112px}
.front-brand{top:257px}
.headline{position:absolute;left:0;right:0;text-align:center;font-family:"Poppins",sans-serif;font-weight:800;letter-spacing:-.5px}
.headline--front{top:336px;font-size:49px;line-height:50px}
.gold{color:var(--gold)}
.navy{color:var(--navy)}
.based{position:absolute;top:448px;left:134px;display:flex;align-items:center;gap:10px;font-family:"Poppins",sans-serif;font-weight:500;font-size:17px;line-height:22px;color:var(--ink)}
.services{position:absolute;top:515px;left:18px;right:14px;display:flex;justify-content:space-between;list-style:none}
.service{display:flex;flex-direction:column;align-items:center;text-align:center;font-size:15px;line-height:16px;color:#222;padding:0 6px;position:relative}
.service + .service::before{content:"";position:absolute;left:-4px;top:4px;height:98px;border-left:1px solid var(--rule)}
.service__icon{width:58px;height:58px;border-radius:50%;background:var(--gold);border:2px solid var(--navy);display:flex;align-items:center;justify-content:center;margin-bottom:12px}
.cta{position:absolute;left:0;bottom:0;width:513px;height:85px}
.cta--back{top:652px;bottom:auto;height:73px}
.cta__call{position:absolute;left:28px;top:14px}
.cta--back .cta__call{top:8px}
.cta__label{display:flex;align-items:center;gap:4px;color:var(--gold);font-family:"Arimo",sans-serif;font-weight:700;font-size:19px;line-height:22px}
.cta__phone{color:var(--white);font-family:"Arimo",sans-serif;font-weight:700;font-size:25px;line-height:28px;margin-top:2px}
.reviews{position:absolute;left:196px;top:10px;padding-left:12px;border-left:1px solid #8da0c4;height:62px;text-align:center;width:130px}
.reviews__name{color:var(--white);font-family:"Poppins",sans-serif;font-weight:700;font-size:18px;line-height:20px}
.reviews__stars{color:var(--gold);font-size:10px;letter-spacing:1px;line-height:10px}
.reviews__count{color:var(--gold);font-weight:700;font-size:16px;margin-top:4px}
.follow{position:absolute;left:362px;top:16px;display:flex;align-items:center;gap:10px;color:var(--navy);font-weight:700;font-size:19px;line-height:19px}
.follow__square{width:30px;height:30px;background:var(--navy);border-radius:4px}
.follow__name{display:block}
.back-brand{top:260px}
.headline--back{top:322px;font-size:40px;line-height:52px;font-weight:700}
.servicing{position:absolute;top:425px;left:28px;right:28px;display:flex;align-items:center;gap:10px;font-family:"Poppins",sans-serif;font-weight:700;font-size:31px;color:var(--ink)}
.servicing::before,.servicing::after{content:"";flex:1;border-top:1.5px solid #555}
.suburbs{position:absolute;top:490px;left:18px;right:18px;display:flex;justify-content:space-between;list-style:none}
.suburb{flex:1;display:flex;flex-direction:column;align-items:center;text-align:center;font-size:14px;font-weight:700;line-height:16px;color:#222;position:relative}
.suburb + .suburb::before{content:"";position:absolute;left:0;top:-8px;height:90px;border-left:1px solid var(--rule)}
.suburb svg{margin-bottom:6px}
.promise{position:absolute;top:597px;left:30px;right:28px;height:41px;border-radius:14px;background:var(--gold);border:1.5px solid var(--navy);color:var(--navy);font-weight:700;font-size:19px;display:flex;align-items:center;justify-content:center}
.contact{position:absolute;left:246px;top:14px;color:var(--navy);font-weight:700;white-space:nowrap}
.contact__web{font-size:14.5px;line-height:18px}
.contact__licence{display:flex;align-items:center;gap:6px;font-size:16px;line-height:20px;margin-top:4px}
</style>
</head>
<body>

<section class="leaflet leaflet--front">
  <div class="hero hero--van" role="img" aria-label="Photo of the branded navy TRV Electrical van parked in the Perth Hills bushland"></div>
  <svg class="frame" width="513" height="725" viewBox="0 0 513 725" aria-hidden="true">
    <polygon points="0,193 145,238 0,343" fill="var(--navy)"/>
    <polygon points="513,203 345,243 513,343" fill="var(--navy)"/>
    <polygon points="0,343 145,238 345,243 513,343 513,725 0,725" fill="var(--white)"/>
    <polygon points="0,640 322,640 350,725 0,725" fill="var(--navy)"/>
    <polygon points="332,648 513,648 513,725 360,725" fill="var(--gold)"/>
  </svg>

  <div class="brand front-brand">
    <span class="brand__mark"></span>
    <span class="brand__name">TRV Electrical Contracting</span>
  </div>

  <h1 class="headline headline--front">
    <span class="gold">WE'RE WORKING</span><br>
    <span class="navy">IN YOUR AREA</span>
  </h1>

  <p class="based">
    <svg width="28" height="40" viewBox="0 0 24 34"><path d="M12 1C6 1 1.5 5.5 1.5 11.5 1.5 19 12 33 12 33s10.5-14 10.5-21.5C22.5 5.5 18 1 12 1z" fill="#e31e24"/><circle cx="12" cy="11.5" r="4.5" fill="#fff"/></svg>
    <span>Local electrician based<br>in Gooseberry Hill</span>
  </p>

  <ul class="services">
    <li class="service">
      <span class="service__icon"><svg width="30" height="30" viewBox="0 0 30 30"><circle cx="12" cy="12" r="8" fill="none" stroke="var(--navy)" stroke-width="3"/><line x1="18" y1="18" x2="27" y2="27" stroke="var(--navy)" stroke-width="4" stroke-linecap="round"/></svg></span>
      Fault<br>finding
    </li>
    <li class="service">
      <span class="service__icon"><svg width="32" height="30" viewBox="0 0 32 30"><rect x="3" y="4" width="26" height="14" rx="2" fill="none" stroke="var(--navy)" stroke-width="2.5"/><circle cx="11" cy="11" r="3" fill="var(--navy)"/><circle cx="21" cy="11" r="3" fill="var(--navy)"/><path d="M16 18v5h8" fill="none" stroke="var(--navy)" stroke-width="2.5"/></svg></span>
      Switchboard<br>upgrades
    </li>
    <li class="service">
      <span class="service__icon"><svg width="28" height="32" viewBox="0 0 28 32"><path d="M14 3a9 9 0 0 0-5 16.5V24h10v-4.5A9 9 0 0 0 14 3z" fill="var(--navy)"/><rect x="9" y="26" width="10" height="3" fill="var(--navy)"/></svg></span>
      Lighting<br>&amp; power
    </li>
    <li class="service">
      <span class="service__icon"><svg width="32" height="32" viewBox="0 0 32 32"><line x1="16" y1="2" x2="16" y2="12" stroke="var(--white)" stroke-width="2.5"/><ellipse cx="16" cy="14" rx="14" ry="2.5" fill="var(--white)"/><line x1="16" y1="16" x2="16" y2="28" stroke="var(--white)" stroke-width="2.5"/><line x1="11" y1="30" x2="21" y2="30" stroke="var(--white)" stroke-width="2.5"/></svg></span>
      Ceiling<br>fans
    </li>
    <li class="service">
      <span class="service__icon"><svg width="32" height="28" viewBox="0 0 32 28"><rect x="3" y="4" width="26" height="6" rx="2" fill="var(--navy)"/><path d="M10 14q2 3 0 6M16 14q2 3 0 6M22 14q2 3 0 6" fill="none" stroke="var(--navy)" stroke-width="2"/></svg></span>
      Smoke alarm<br>compliance
    </li>
  </ul>

  <div class="cta">
    <div class="cta__call">
      <div class="cta__label"><svg width="20" height="20" viewBox="0 0 24 24"><path d="M6.6 10.8a15 15 0 0 0 6.6 6.6l2.2-2.2a1 1 0 0 1 1-.25 11.4 11.4 0 0 0 3.6.57 1 1 0 0 1 1 1V20a1 1 0 0 1-1 1A17 17 0 0 1 3 4a1 1 0 0 1 1-1h3.5a1 1 0 0 1 1 1c0 1.25.2 2.45.57 3.57a1 1 0 0 1-.25 1z" fill="var(--gold)"/></svg>Call Dorian</div>
      <div class="cta__phone">0472 615 904</div>
    </div>
    <div class="reviews">
      <div class="reviews__name">Rovlix</div>
      <div class="reviews__stars">★★★★★</div>
      <div class="reviews__count">110+ Reviews</div>
    </div>
    <div class="follow">
      <span><span class="follow__name">Follow</span>us on</span>
      <span class="follow__square"></span>
    </div>
  </div>
</section>

<section class="leaflet leaflet--back">
  <div class="hero hero--switchboard" role="img" aria-label="Photo of an electrician in a hard hat working on a switchboard"></div>
  <svg class="frame" width="513" height="725" viewBox="0 0 513 725" aria-hidden="true">
    <polygon points="0,193 150,238 0,343" fill="var(--navy)"/>
    <polygon points="513,203 345,243 513,343" fill="var(--navy)"/>
    <polygon points="0,343 150,238 345,243 513,343 513,725 0,725" fill="var(--white)"/>
    <polygon points="0,652 212,652 232,725 0,725" fill="var(--navy)"/>
    <polygon points="222,660 513,660 513,725 242,725" fill="var(--gold)"/>
  </svg>

  <div class="brand back-brand">
    <span class="brand__mark"></span>
    <span class="brand__name brand__name--small">TRV Electrical Contracting</span>
  </div>

  <h2 class="headline headline--back">
    <span class="gold">Your</span> <span class="navy">Local Perth</span><br>
    <span class="navy">Hills</span> <span class="gold">Electrician</span>
  </h2>

  <p class="servicing">Servicing</p>

  <ul class="suburbs">
    <li class="suburb"><svg width="32" height="44" viewBox="0 0 24 34"><path d="M12 1C6 1 1.5 5.5 1.5 11.5 1.5 19 12 33 12 33s10.5-14 10.5-21.5C22.5 5.5 18 1 12 1z" fill="var(--navy)"/><circle cx="12" cy="11.5" r="4.5" fill="#fff"/></svg>Kalamunda</li>
    <li class="suburb"><svg width="32" height="44" viewBox="0 0 24 34"><path d="M12 1C6 1 1.5 5.5 1.5 11.5 1.5 19 12 33 12 33s10.5-14 10.5-21.5C22.5 5.5 18 1 12 1z" fill="var(--gold)"/><circle cx="12" cy="11.5" r="4.5" fill="#fff"/></svg>Gooseberry<br>Hill</li>
    <li class="suburb"><svg width="32" height="44" viewBox="0 0 24 34"><path d="M12 1C6 1 1.5 5.5 1.5 11.5 1.5 19 12 33 12 33s10.5-14 10.5-21.5C22.5 5.5 18 1 12 1z" fill="var(--navy)"/><circle cx="12" cy="11.5" r="4.5" fill="#fff"/></svg>Lesmurdie</li>
    <li class="suburb"><svg width="32" height="44" viewBox="0 0 24 34"><path d="M12 1C6 1 1.5 5.5 1.5 11.5 1.5 19 12 33 12 33s10.5-14 10.5-21.5C22.5 5.5 18 1 12 1z" fill="var(--gold)"/><circle cx="12" cy="11.5" r="4.5" fill="#fff"/></svg>Walliston</li>
    <li class="suburb"><svg width="32" height="44" viewBox="0 0 24 34"><path d="M12 1C6 1 1.5 5.5 1.5 11.5 1.5 19 12 33 12 33s10.5-14 10.5-21.5C22.5 5.5 18 1 12 1z" fill="var(--navy)"/><circle cx="12" cy="11.5" r="4.5" fill="#fff"/></svg>Pickering<br>Brook</li>
  </ul>

  <p class="promise">Reliable electrical work across the Perth Hills.</p>

  <div class="cta cta--back">
    <div class="cta__call">
      <div class="cta__label"><svg width="20" height="20" viewBox="0 0 24 24"><path d="M6.6 10.8a15 15 0 0 0 6.6 6.6l2.2-2.2a1 1 0 0 1 1-.25 11.4 11.4 0 0 0 3.6.57 1 1 0 0 1 1 1V20a1 1 0 0 1-1 1A17 17 0 0 1 3 4a1 1 0 0 1 1-1h3.5a1 1 0 0 1 1 1c0 1.25.2 2.45.57 3.570a1 1 0 0 1-.25 1z" fill="var(--gold)"/></svg>Call Dorian</div>
      <div class="cta__phone">0472 615 904</div>
    </div>
    <div class="contact">
      <div class="contact__web">www.trvelectrical-example.com.au</div>
      <div class="contact__licence"><svg width="20" height="14" viewBox="0 0 20 14"><rect x="1" y="1" width="18" height="12" rx="1.5" fill="none" stroke="var(--navy)" stroke-width="2"/><rect x="4" y="4" width="5" height="6" fill="var(--navy)"/><line x1="11" y1="5" x2="16" y2="5" stroke="var(--navy)" stroke-width="1.6"/><line x1="11" y1="9" x2="16" y2="9" stroke="var(--navy)" stroke-width="1.6"/></svg>EC47286</div>
    </div>
  </div>
</section>

</body>
</html>
```